Modern Lawfirm Business Card Design

We're looking for a business card to incorporate the newly created logo we had made.

Ideally looking for a law firm business card demonstrating, modern, minimalist, strong/bold design.

I'm open to any design honestly, but nothing "flashy".

Target Market(s)

Immigration law, family immigration, humanitarian, general legal

Industry/Entity Type

Law Firm

Contact Information for Business Card

Please use dummy information, name, street address, city, state, phone number, email, website.

Font styles to use
Serif
Sans Serif

Requirements
Must have
• Please use dummy information, name, street address, city, state, phone number, email, website.

```html
<!DOCTYPE html>
<html lang="en">
<head>
<meta charset="utf-8">
<title>Marlow Business Card</title>
<link href="https://fonts.googleapis.com/css2?family=Lora:wght@400;500&display=swap" rel="stylesheet">
<style>
  :root {
    --page-bg: #e9e6e1;
    --panel-light-top: #f4f4f6;
    --panel-light-bottom: #dcdadb;
    --panel-navy: #143070;
    --panel-navy-deep: #0b1b45;
    --brand-navy: #1d3a78;
    --accent-tan: #d8c7ad;
    --accent-tan-soft: #c9b79c;
    --icon-ink: #0f2458;
  }
  * { margin: 0; padding: 0; box-sizing: border-box; }
  html, body {
    width: 1200px;
    height: 970px;
    overflow: hidden;
    background: var(--page-bg);
    font-family: "Lora", Georgia, serif;
  }
  .canvas {
    position: relative;
    width: 1200px;
    height: 970px;
  }
  .card {
    position: absolute;
    left: 100px;
    top: 200px;
    width: 1000px;
    height: 570px;
    display: flex;
    box-shadow: 0 18px 40px rgba(0,0,0,0.18);
  }
  .card__brand-side {
    width: 500px;
    height: 100%;
    background: linear-gradient(180deg, var(--panel-light-top), var(--panel-light-bottom));
    display: flex;
    align-items: center;
    justify-content: center;
    gap: 16px;
  }
  .brand-mark {
    width: 22px;
    height: 22px;
    background: var(--brand-navy);
  }
  .brand-name {
    color: var(--brand-navy);
    font-size: 60px;
    font-weight: 500;
    letter-spacing: 2px;
  }
  .card__info-side {
    width: 500px;
    height: 100%;
    background: linear-gradient(200deg, var(--panel-navy) 0%, #102a63 45%, var(--panel-navy-deep) 100%);
    padding: 140px 0 0 52px;
    color: var(--accent-tan);
  }
  .person-name {
    font-size: 36px;
    font-weight: 500;
    letter-spacing: 1px;
    line-height: 1.1;
  }
  .person-title {
    font-size: 26px;
    color: var(--accent-tan-soft);
    line-height: 1.3;
  }
  .address {
    margin-top: 38px;
    font-size: 26px;
    line-height: 1.32;
  }
  .contacts {
    margin-top: 22px;
    list-style: none;
    font-size: 26px;
    line-height: 1.3;
  }
  .contacts li {
    display: flex;
    align-items: center;
    gap: 12px;
  }
  .contact-icon {
    width: 28px;
    height: 28px;
    flex: none;
  }
</style>
</head>
<body>
<div class="canvas">
  <div class="card">
    <div class="card__brand-side">
      <span class="brand-mark"></span>
      <span class="brand-name">MARLOW</span>
    </div>
    <div class="card__info-side">
      <div class="person-name">DANIEL REYES</div>
      <div class="person-title">Managing Director</div>
      <div class="address">PO BOX 418 Harbor Lane<br>Suite 210 Denver, CO USA</div>
      <ul class="contacts">
        <li>
          <svg class="contact-icon" viewBox="0 0 28 28" aria-hidden="true">
            <rect width="28" height="28" fill="#d8c7ad"/>
            <path d="M7 12 Q14 6 21 12 L19 14 L17 12 L11 12 L9 14 Z" fill="#0f2458"/>
            <rect x="8" y="14" width="12" height="7" rx="1" fill="#0f2458"/>
          </svg>
          (303) 555 0142
        </li>
        <li>
          <svg class="contact-icon" viewBox="0 0 28 28" aria-hidden="true">
            <rect width="28" height="28" fill="#d8c7ad"/>
            <rect x="6" y="8" width="16" height="12" fill="none" stroke="#0f2458" stroke-width="1.6"/>
            <path d="M6 8 L14 15 L22 8" fill="none" stroke="#0f2458" stroke-width="1.6"/>
          </svg>
          info@marlowlaw.com
        </li>
        <li>
          <svg class="contact-icon" viewBox="0 0 28 28" aria-hidden="true">
            <rect width="28" height="28" fill="#d8c7ad"/>
            <circle cx="14" cy="14" r="8" fill="none" stroke="#0f2458" stroke-width="1.5"/>
            <ellipse cx="14" cy="14" rx="3.5" ry="8" fill="none" stroke="#0f2458" stroke-width="1.2"/>
            <line x1="6" y1="14" x2="22" y2="14" stroke="#0f2458" stroke-width="1.2"/>
          </svg>
          www.marlowlaw.com
        </li>
      </ul>
    </div>
  </div>
</div>
</body>
</html>
```